On Demand Digital Interview Lunch and Learn Event Flyer

We are hosting a lunch and learn for prospects to introduce our Digital Interview process - attendees are Human Resource and Hiring Managers.

We need a flyer that we can email and also have printed (large postcard size) to be either mailed out or dropped off at a prospects location. I have included a picture of a Digital Interview to be used on the flyer (people don't get it till they see it) as well as content. Please feel free to rewrite, restructure, the content to produce a good flow.

Return address on the back (the one we would print) is RL Workforce - 2740 Halden Road - Suite 318 - Nashville, TN 37482

Target Market(s)

Business Owners, Human Resource Managers

Industry/Entity Type

Digital

Font styles to use
Sans Serif

Requirements
Must have
• Must be clean and professional with plenty of white space

```html
<!DOCTYPE html>
<html lang="en">
<head>
<meta charset="utf-8">
<title>Digital Interviews Lunch and Learn – Postcard</title>
<link rel="stylesheet" href="https://fonts.googleapis.com/css2?family=Roboto+Condensed:wght@400;700&display=swap">
<style>
  :root {
    --bg: #e6e6e6;
    --red: #e0343f;
    --red-soft: #ea5560;
    --teal: #1fae8e;
    --white: #ffffff;
    --photo-warm-a: #e98a8f;
    --photo-warm-b: #8a5a58;
    --photo-warm-c: #3d3633;
    --photo-cool-a: #dfe8ef;
    --photo-cool-b: #a9bccb;
  }
  * { box-sizing: border-box; margin: 0; padding: 0; }
  html, body { width: 1200px; height: 960px; overflow: hidden; }
  body {
    background: var(--bg);
    font-family: "Roboto Condensed", Arial, sans-serif;
    position: relative;
  }
  .postcard {
    position: absolute;
    width: 640px;
    height: 416px;
    overflow: hidden;
    background: var(--white);
    box-shadow: 0 6px 18px rgba(0,0,0,.18);
  }
  .postcard--front { left: 60px; top: 40px; }
  .postcard--back { left: 500px; top: 496px; }

  /* Front */
  .front-photo {
    position: absolute; inset: 0;
    background: linear-gradient(115deg, var(--photo-warm-a) 0%, #c9757a 40%, var(--photo-warm-b) 70%, var(--photo-warm-c) 100%);
  }
  .brand-tile {
    position: absolute; left: 0; top: 24px;
    background: var(--white);
    padding: 12px 12px;
    display: flex; align-items: center; gap: 6px;
  }
  .brand-mark { width: 10px; height: 10px; background: var(--red); }
  .brand-name {
    color: var(--red); font-weight: 700; font-size: 18px; letter-spacing: .2px;
    white-space: nowrap;
  }
  .title-frame {
    position: absolute; left: 100px; top: 146px;
    width: 440px;
    border: 1.5px solid rgba(255,255,255,.85);
    text-align: center; color: var(--white);
    padding: 16px 10px 14px;
    white-space: nowrap;
  }
  .title-main { font-size: 36px; font-weight: 700; line-height: 1; letter-spacing: .3px; }
  .title-sub { font-size: 18px; letter-spacing: 1px; margin-top: 6px; line-height: 1.1; }
  .event-details {
    position: absolute; left: 0; right: 0; top: 262px;
    text-align: center; color: var(--white);
    font-size: 18px; line-height: 1.3; letter-spacing: .6px;
    white-space: nowrap;
  }
  .event-details sup { font-size: 11px; }
  .contact-band {
    position: absolute; left: 0; right: 0; bottom: 0; height: 40px;
    background: var(--red); color: var(--white);
    font-size: 13px; letter-spacing: .2px; white-space: nowrap;
    display: flex; align-items: center; justify-content: center;
  }

  /* Back */
  .back-left { position: absolute; left: 0; top: 0; width: 390px; height: 416px; }
  .back-photo {
    position: absolute; left: 0; top: 0; width: 390px; height: 230px;
    background: linear-gradient(160deg, var(--photo-cool-a) 0%, #c9d6e0 55%, var(--photo-cool-b) 100%);
  }
  .back-left .brand-tile { left: auto; right: 0; top: 0; padding: 8px 10px; }
  .back-left .brand-name { font-size: 15px; }
  .back-heading {
    position: absolute; left: 0; top: 176px; width: 390px; height: 72px;
    background: rgba(255,255,255,.75);
    text-align: center; color: var(--red); padding-top: 10px;
    white-space: nowrap;
  }
  .back-title { font-size: 30px; font-weight: 700; line-height: 1; }
  .back-subtitle { font-size: 15px; letter-spacing: 1px; margin-top: 3px; }
  .back-copy {
    position: absolute; left: 0; top: 248px; width: 390px; height: 168px;
    background: var(--teal); color: var(--white);
    padding: 18px 22px;
    font-size: 12.5px; line-height: 1.4; text-transform: uppercase; text-align: center;
  }
  .mail-side { position: absolute; left: 390px; top: 0; width: 250px; height: 416px; background: var(--red); }
  .stamp-box { position: absolute; left: 0; top: 20px; width: 110px; height: 120px; background: var(--red-soft); }
  .address-lines { position: absolute; left: 0; top: 0; }
</style>
</head>
<body>

<section class="postcard postcard--front" aria-label="Postcard front">
  <div class="front-photo" role="img" aria-label="Photo of a person typing on a laptop at a wooden café table with a coffee cup, tinted pink"></div>
  <div class="brand-tile">
    <span class="brand-mark"></span>
    <span class="brand-name">RL Workforce</span>
  </div>
  <div class="title-frame">
    <h1 class="title-main">HOW DIGITAL INTERVIEWS</h1>
    <p class="title-sub">CAN PRODUCE BETTER CANDIDATES</p>
  </div>
  <p class="event-details">
    LINDEN COUNTY CHAMBER OF COMMERCE<br>
    11:30 - 1:00PM - / WEDNESDAY, AUGUST 24<sup>TH</sup>
  </p>
  <div class="contact-band">JORDAN.AMES@RLWORKFORCE.COM OR CALL 615 555-0148 FOR MORE INFORMATION.</div>
</section>

<section class="postcard postcard--back" aria-label="Postcard back">
  <div class="back-left">
    <div class="back-photo" role="img" aria-label="Photo of a job candidate on a video interview with three hiring managers on screen"></div>
    <div class="brand-tile">
      <span class="brand-mark"></span>
      <span class="brand-name">RL Workforce</span>
    </div>
    <div class="back-heading">
      <h2 class="back-title">HOW DIGITAL INTERVIEWS</h2>
      <p class="back-subtitle">CAN PRODUCE BETTER CANDIDATES</p>
    </div>
    <p class="back-copy">
      On demand digital interviews offer individuals the ability to share their stories and demonstrate their work through video – all on their own time by using a computer, tablet, or smartphone. More than 60% of interviews take place outside of the normal 9-5 business hours. Learn how hiring managers can save time, qualify more candidates, and can get a better overall first impression before setting up a first round interview.
    </p>
  </div>
  <div class="mail-side">
    <svg class="address-lines" width="250" height="416" viewBox="0 0 250 416" aria-hidden="true">
      <g stroke="rgba(255,255,255,0.18)" stroke-width="1">
        <line x1="0" y1="40" x2="250" y2="40"/>
        <line x1="0" y1="80" x2="250" y2="80"/>
        <line x1="0" y1="120" x2="250" y2="120"/>
        <line x1="0" y1="160" x2="250" y2="160"/>
        <line x1="0" y1="200" x2="250" y2="200"/>
      </g>
    </svg>
    <div class="stamp-box"></div>
  </div>
</section>

</body>
</html>
```